Women's Online Clothing Boutique Needs Business Cards

I already have a logo that I would like to use. Some of the things that interest me is black business cards, foil embossed logo, glossy embossed logo, leopard print, no yellow font, rounded edges. I even like just a large logo on the front side with all of my information on the back side.

Contact Information for Business Card

https://silverheron.shopvenlo.com/
https://www.pagelink.net/thesilverheronboutique/
https://www.picfeed.net/thesilverheronboutique/
silverheronboutique@mailora.net

Requirements
Must have
• My Logo
Nice to have
• Leopard Print
Should not have
• No Yellow Font

```html
<!DOCTYPE html>
<html lang="en">
<head>
<meta charset="utf-8">
<title>The Silver Heron Boutique — Business Cards</title>
<link href="https://fonts.googleapis.com/css2?family=Montserrat:wght@500;700&family=Kaushan+Script&display=swap" rel="stylesheet">
<style>
  :root {
    --backdrop: #e3e3e3;
    --card: #1b1b1c;
    --card-edge: #242425;
    --foil: #cfcfcf;
    --foil-soft: #a9a9a9;
    --ink-light: #e6e6e6;
  }
  * { margin: 0; padding: 0; box-sizing: border-box; }
  html, body {
    width: 1200px; height: 1200px; overflow: hidden;
    background: var(--backdrop);
    font-family: "Montserrat", Arial, sans-serif;
  }
  .sheet { position: relative; width: 1200px; height: 1200px; }
  .card {
    position: absolute; left: 262px; width: 685px; height: 392px;
    border-radius: 24px;
    background: linear-gradient(160deg, var(--card-edge), var(--card) 60%);
    box-shadow: 0 18px 30px rgba(0,0,0,0.25);
  }
  .card--front { top: 165px; }
  .card--back { top: 652px; }

  .brand-lockup {
    position: absolute; left: 0; right: 0; top: 170px;
    display: flex; align-items: center; justify-content: center; gap: 14px;
  }
  .brand-dot {
    width: 18px; height: 18px; border-radius: 50%; background: var(--foil);
  }
  .brand-name {
    font-weight: 500; font-size: 38px; letter-spacing: 0.5px;
    color: var(--foil); white-space: nowrap;
  }
  .brand-rule {
    position: absolute; left: 128px; right: 128px; top: 262px;
    height: 1px; background: var(--foil-soft); opacity: 0.6;
  }

  .back-brand {
    position: absolute; left: 100px; top: 178px;
    display: flex; align-items: center; gap: 10px;
  }
  .back-brand .brand-dot { width: 12px; height: 12px; }
  .back-brand .brand-name { font-size: 21px; }

  .contact-block { position: absolute; left: 353px; top: 144px; color: var(--ink-light); }
  .person-name {
    font-weight: 700; font-size: 21px; letter-spacing: 1px; color: var(--foil);
  }
  .person-role {
    font-family: "Kaushan Script", cursive; font-size: 15px; color: var(--ink-light);
    margin-top: 2px;
  }
  .contact-list { list-style: none; margin-top: 22px; }
  .contact-list li {
    display: flex; align-items: center; gap: 12px;
    font-size: 14.5px; font-weight: 500; line-height: 20px;
  }
  .contact-list svg { width: 10px; height: 10px; fill: var(--foil); flex: none; }
</style>
</head>
<body>
<div class="sheet">
  <section class="card card--front" aria-label="Card front">
    <div class="brand-lockup">
      <span class="brand-dot"></span>
      <span class="brand-name">The Silver Heron Boutique</span>
    </div>
    <div class="brand-rule"></div>
  </section>

  <section class="card card--back" aria-label="Card back">
    <div class="back-brand">
      <span class="brand-dot"></span>
      <span class="brand-name">The Silver Heron</span>
    </div>
    <div class="contact-block">
      <div class="person-name">DANIEL BROOKS</div>
      <div class="person-role">President</div>
      <ul class="contact-list">
        <li><svg viewBox="0 0 10 10"><path d="M2 0.5 L3.8 2.6 L2.9 3.6 Q4 6 6.4 7.1 L7.4 6.2 L9.5 8 L8.3 9.5 Q1.5 8.5 0.5 1.7 Z"/></svg>555-214-7730</li>
        <li><svg viewBox="0 0 10 10"><path d="M0 2 H10 V8.5 H0 Z M0.8 2.6 L5 5.6 L9.2 2.6 V3.4 L5 6.4 L0.8 3.4 Z" fill-rule="evenodd"/></svg>info@thesilverheron.net</li>
        <li><svg viewBox="0 0 10 10"><circle cx="5" cy="5" r="4.5"/></svg>thesilverheron.net</li>
      </ul>
    </div>
  </section>
</div>
</body>
</html>
```